New Website for QWRB Holdings (Property Leasing Company in New Haven)

Design a fully functioning website for a real estate property leasing company. The company has a few properties in New Haven, CT and would like to provide an option for its tenants to pay their rent online. The company should have the ability to generate unique account log in username and password for its tenants so they can make online payments through ACH the website. (The ACH processing part will be coordinated with the bank).

Please take a look at all the pictures I uploaded of New Haven especially the area around Marlow College, you will find that the general style is Gothic and charming.

Also please make use of the pictures of the two properties I have attached to the description.

Please keep Holdings page, Contact Us Page , About Us Page, and please add a page entitled "Tenants".

On the Holdings page I would like to see on the left hand side an interactive map of new haven (Please see a map attached), split by New Haven's neighbourhoods, and showing my properties as pins of sort on the map (I can send you the addresses of the properties upon request). On the same page on the right side I want to see a drop down menu that includes list of New Haven Neighbourhoods. When a neighbourhood is selected you can see in the space underneath the drop-down menu the properties we have in that neighbourhood in large thumbnail format. Also on the map you can see the pins corresponding to those properties change colour. A user can either click on the pin or on the thumbnails to have view more pictures of the property and some details in text.

The tenants page should prompt a login to access- I like your idea of having the company name in two colours, one for QWRB and another for Holdings.Please let me know if you have any questions along the way

-------------------------------------------------------------------------------
Property Descriptions for Holdings Page
The Larch Lodge,

Neighbourhood: Westville
Name: Silas Brennaway House
Building Style: Queen Anne Style
Address: 418 Pellwin Road, New Haven, CT 06515
Number of Units: 3
Unit Names: Unit 1, Unit 2, Unit 3

Property Description

This Westiville home was built in 1897, historically known as The Silas Brennaway House, it is an example of the Queen Anne style. The large carriage house is still intact and sits in the lovely, expansive back garden! An outstanding architectural feature of the house is the turret, giving the home prominence on Pellwin Road. This well maintained home has renovated kitchens in all units, the first floor has granite and red oak cabinetry. New baths and central air in all apartments. All newer mechanicals for each unit, all natural gas. The entire house has replacement windows. The new back deck overlooks the back garden and carriage house. The front steps and porch have also been rebuilt. Roof has 30 year architectural singles and approximately 15 years old, the chimney has just been lined.

Unit 1 Description:

2 Bedrooms, 6 rooms in total.
Amenities: Dishwasher, Central Air, Gas Heating, Porch

Unit 2 Description:

2 Bedrooms, 5 rooms in total.
Amenities: Dishwasher, Central Air, Gas Heating, Balcony

Unit 3 Description:

2 Bedrooms, 4 rooms in total.
Amenities: Dishwasher, Central Air, Gas Heating

The Fern Lodge:

Neighbourhood: East Rock
Name: 64 Birchmere
Building Style: Victorian
Address: 64 Birchmere Lane, New Haven, CT 06511
Number of Units: 2
Unit Names: Unit 1, and Unit 2

Property Description

East Rock incredibly charming newly renovated 2 family on quiet tree-lined block. Tenants are responsible for all utilities (gas heat, electricity and cable). Small pets are possible with landlord approval. Tenants has use of shared yard, laundry in the basement and on street parking only. Located steps away from gourmet markets & minutes to Downtown New Haven, Marlow & local hospitals. Fascinating backyard. This is a feel good house!

Unit 1 Description:

Area:
1100 soft, 3 Bedrooms, 5 rooms in total.
Amenities: In unit Washer and Dryer, Central Air, Gas Heating, Porch, Backyard

Unit 2 Description:

Area: 2,820 sqft
5 Bedrooms, 8 rooms in total.
Amenities: In unit Washer and Dryer, Dishwasher, Central Air, and Gas Heating

Target Market(s)

1-3 bedroom Renting Market around Marlow College and New Haven Community

Industry/Entity Type

Real Estate

Coding

Coded - Design and coding required

Number of Pages Required

4 page

Font styles to use
Other font styles liked:
• Helvetica

Colors
85cae6
cee9f5
d9d9d9
9d9d9d

Requirements
Must have
• Payment page with login (accounts can only be created by administrator)
• A page showcasing the properties (Professional photos to be uploaded shortly)
• A page for technical support, contact information and so forth
• Home page
Nice to have
• A professional, but stylish design. Not too colourful, something with pastel colours
Should not have
• A lot of colours, any pop-ups,

```html
<!DOCTYPE html>
<html lang="en">
<head>
<meta charset="utf-8">
<title>QWRB Holdings — Specializing in Faster Leasing</title>
<link rel="stylesheet" href="https://fonts.googleapis.com/css2?family=Open+Sans:wght@400;600;700;800&display=swap">
<style>
:root{
  --blue:#4fb3de;
  --blue-soft:#85cae6;
  --blue-pale:#cee9f5;
  --grey-line:#d9d9d9;
  --grey-text:#9d9d9d;
  --ink:#333a3f;
  --body:#6f767b;
  --band:#f2f2f2;
  --price:#f39c12;
  --footer:#2f4651;
  --footer-deep:#253a44;
  --footer-text:#a9b8bf;
  --white:#ffffff;
}
*{box-sizing:border-box;margin:0;padding:0}
html,body{width:1200px;height:2584px;overflow:hidden}
body{font-family:"Open Sans",Helvetica,Arial,sans-serif;color:var(--body);background:var(--white);font-size:13px;line-height:1.5}
.wrap{width:944px;margin:0 auto;position:relative}

/* header */
.site-header{height:64px;background:var(--white);border-bottom:1px solid var(--grey-line)}
.site-header .wrap{display:flex;align-items:center;height:64px}
.brand{display:flex;align-items:center;gap:8px;font-weight:800;font-size:22px;color:var(--blue);letter-spacing:.3px}
.brand-mark{width:14px;height:14px;background:var(--blue)}
.main-nav{margin-left:auto;display:flex;gap:26px;align-items:center}
.main-nav a{font-size:11px;font-weight:600;color:var(--ink);text-decoration:none;letter-spacing:.4px}
.main-nav a.is-active{color:var(--blue)}
.btn-login{margin-left:26px;background:var(--blue);color:var(--white);font-size:11px;font-weight:700;padding:6px 14px;border-radius:3px;display:flex;align-items:center;gap:6px}

/* hero */
.hero{height:436px;position:relative;background:linear-gradient(180deg,#33506a 0%,#5e7c94 30%,#c9d3d8 62%,#7b8b7a 82%,#4a5a4c 100%)}
.hero-photo{position:absolute;inset:0}
.hero-copy{position:absolute;top:92px;left:0;right:0;text-align:center}
.hero-copy h1{color:var(--white);font-size:50px;font-weight:800;letter-spacing:.5px;text-shadow:0 2px 6px rgba(0,0,0,.35)}
.btn{display:inline-block;background:var(--blue);color:var(--white);font-size:12px;font-weight:700;padding:9px 22px;border-radius:3px;letter-spacing:.4px}
.hero-copy .btn{margin-top:14px}
.find-tab{position:absolute;left:128px;bottom:0;background:rgba(40,52,60,.85);color:var(--white);font-size:15px;font-weight:700;padding:10px 26px;display:flex;align-items:center;gap:10px}

/* search */
.search{padding:26px 0 18px}
.search-row{display:flex;gap:14px;margin-bottom:16px}
.field{flex:1;height:34px;border:1px solid var(--grey-line);border-radius:3px;display:flex;align-items:center;justify-content:space-between;padding:0 12px;font-size:11px;color:var(--grey-text)}
.field svg{width:9px;height:6px}
.search-row .spacer{flex:1}
.btn-search{flex:1;height:34px;background:var(--blue);color:var(--white);font-weight:700;font-size:12px;display:flex;align-items:center;justify-content:center;border-radius:3px}

/* section heads */
.section-head{text-align:center}
.section-head h2{font-size:20px;font-weight:700;color:var(--blue);letter-spacing:.5px}
.section-head p{font-size:11px;color:var(--grey-text);margin-top:4px}

/* most popular */
.popular{height:620px;padding-top:36px;border-top:1px solid var(--grey-line)}
.popular-grid{width:720px;margin:36px auto 0;display:grid;grid-template-columns:1fr 1fr;gap:24px 28px}
.listing{display:flex;border:1px solid var(--grey-line);height:180px;flex-wrap:wrap}
.listing .thumb{width:130px;height:140px;margin:0}
.listing-body{flex:1;padding:10px 12px 0}
.listing h3{font-size:13px;font-weight:700;color:var(--ink)}
.listing p{font-size:10px;line-height:1.45;margin-top:4px}
.price{color:var(--price);font-weight:700;font-size:13px;margin-top:6px}
.listing-meta{width:100%;height:38px;border-top:1px solid var(--grey-line);display:flex;gap:22px;align-items:center;padding-left:140px;font-size:10px;color:var(--body)}
.listing-meta span{display:flex;align-items:center;gap:6px}
.load-more{display:block;width:100px;margin:32px auto 0;text-align:center;border:1px solid var(--grey-line);color:var(--grey-text);font-size:11px;padding:6px 0;border-radius:3px}

/* featured */
.featured{height:488px;background:var(--band);padding-top:40px}
.featured-grid{display:grid;grid-template-columns:repeat(4,1fr);gap:16px;margin-top:34px}
.feature-card{background:var(--white);border:1px solid var(--grey-line)}
.feature-card .thumb{height:150px}
.feature-body{padding:12px 12px 14px}
.feature-body h3{font-size:13px;font-weight:700;color:var(--ink)}
.feature-body p{font-size:10px;margin-top:3px;line-height:1.45}

/* news and testimonial */
.lower{height:400px;padding-top:36px}
.lower .wrap{display:flex;gap:60px}
.col-head{font-size:18px;font-weight:700;color:var(--blue);letter-spacing:.4px;padding-bottom:10px;border-bottom:1px solid var(--grey-line)}
.news{width:432px}
.news-item{display:flex;gap:16px;margin-top:20px}
.news-item .thumb{width:132px;height:100px;flex:none}
.news-item h3{font-size:13px;font-weight:600;color:var(--ink);line-height:1.35}
.news-item .date{font-size:10px;color:var(--grey-text);margin-top:2px}
.news-item p{font-size:10px;margin-top:4px;line-height:1.45}
.testimonial{flex:1}
.quote-box{margin-top:22px;border:1px solid var(--grey-line);padding:22px 24px;font-size:11px;font-style:italic;line-height:1.7;position:relative}
.quote-box::after{content:"";position:absolute;right:60px;bottom:-9px;width:16px;height:16px;background:var(--white);border-right:1px solid var(--grey-line);border-bottom:1px solid var(--grey-line);transform:rotate(45deg)}
.client{display:flex;align-items:center;justify-content:flex-end;gap:14px;margin-top:18px}
.client-name{color:var(--blue);font-weight:700;font-size:12px}
.client .avatar{width:56px;height:56px;border-radius:50%;background:linear-gradient(135deg,#d9c4ae,#9a8878)}

/* footer */
.site-footer{height:368px;background:var(--footer);color:var(--footer-text);padding-top:50px}
.site-footer .wrap{display:flex;gap:40px}
.foot-col{font-size:10px;line-height:1.6}
.foot-about{width:260px}
.foot-about .brand{font-size:20px;margin-bottom:14px}
.foot-about .more{color:var(--white);font-weight:600;margin-top:18px;display:block}
.foot-col h4{color:var(--white);font-size:16px;font-weight:600;margin-bottom:14px}
.foot-links{width:130px}
.foot-links li{list-style:none;padding:3px 0}
.foot-news{width:200px}
.foot-input{height:28px;background:var(--footer-deep);margin-top:12px;padding:0 10px;display:flex;align-items:center;color:#7f949d}
.foot-submit{display:inline-block;margin-top:8px;background:var(--blue);color:var(--white);font-weight:700;padding:4px 12px;border-radius:2px}
.foot-contact{flex:1}
.contact-row{display:flex;align-items:center;gap:12px;margin-bottom:14px}
.contact-row .ico{width:26px;height:26px;border-radius:50%;background:var(--footer-deep);display:flex;align-items:center;justify-content:center}
.contact-row svg{width:12px;height:12px}
.copyright{height:56px;background:var(--footer-deep);color:var(--footer-text);font-size:10px;display:flex;align-items:center;justify-content:center}
</style>
</head>
<body>

<header class="site-header">
  <div class="wrap">
    <div class="brand"><span class="brand-mark"></span>QWRB Holdings</div>
    <nav class="main-nav">
      <a class="is-active" href="#">HOME</a>
      <a href="#">ABOUT US</a>
      <a href="#">PROPERTIES</a>
      <a href="#">NEWS</a>
      <a href="#">SERVICES</a>
      <a href="#">CONTACT US</a>
    </nav>
    <div class="btn-login">
      <svg width="10" height="10" viewBox="0 0 10 10"><circle cx="5" cy="3" r="2.2" fill="#fff"/><path d="M1 10c0-2.5 1.8-4 4-4s4 1.5 4 4z" fill="#fff"/></svg>LOGIN
    </div>
  </div>
</header>

<section class="hero">
  <div class="hero-photo" role="img" aria-label="Modern white villa under a blue sky with palm trees"></div>
  <div class="hero-copy">
    <h1>SPECIALIZING IN FASTER LEASING</h1>
    <span class="btn">GET STARTED</span>
  </div>
  <div class="find-tab">
    <svg width="16" height="16" viewBox="0 0 16 16"><circle cx="6.5" cy="6.5" r="4.5" fill="none" stroke="#fff" stroke-width="2"/><path d="M10 10l4.5 4.5" stroke="#fff" stroke-width="2"/></svg>
    FIND A PROPERTY
  </div>
</section>

<section class="search">
  <div class="wrap">
    <div class="search-row">
      <div class="field">Location<svg viewBox="0 0 9 6"><path d="M0 0h9L4.5 6z" fill="#9d9d9d"/></svg></div>
      <div class="field">Status<svg viewBox="0 0 9 6"><path d="M0 0h9L4.5 6z" fill="#9d9d9d"/></svg></div>
      <div class="field">Property Type<svg viewBox="0 0 9 6"><path d="M0 0h9L4.5 6z" fill="#9d9d9d"/></svg></div>
      <div class="spacer"></div>
    </div>
    <div class="search-row">
      <div class="field">Bedrooms<svg viewBox="0 0 9 6"><path d="M0 0h9L4.5 6z" fill="#9d9d9d"/></svg></div>
      <div class="field">Bathrooms<svg viewBox="0 0 9 6"><path d="M0 0h9L4.5 6z" fill="#9d9d9d"/></svg></div>
      <div class="field">Min Price<svg viewBox="0 0 9 6"><path d="M0 0h9L4.5 6z" fill="#9d9d9d"/></svg></div>
      <div class="field">Max Price<svg viewBox="0 0 9 6"><path d="M0 0h9L4.5 6z" fill="#9d9d9d"/></svg></div>
      <div class="btn-search">Search</div>
    </div>
  </div>
</section>

<section class="popular">
  <div class="section-head">
    <h2>MOST POPULAR</h2>
    <p>Homes our tenants viewed most often during this past leasing season.</p>
  </div>
  <div class="popular-grid">
    <article class="listing">
      <div class="thumb" role="img" aria-label="Bright apartment living room with yellow sofa" style="background:linear-gradient(135deg,#e7c66a,#b78a52)"></div>
      <div class="listing-body">
        <h3>Los Angeles Appartement</h3>
        <p>We are one of the best agents in the area that genuinely are specialist in both sales and lettings.</p>
        <div class="price">$10,000</div>
      </div>
      <div class="listing-meta">
        <span><svg width="14" height="9" viewBox="0 0 14 9"><path d="M0 0v9M0 6h14v3M3 3h10v3" stroke="#6f767b" fill="none" stroke-width="1.4"/></svg>3 Bedrooms</span>
        <span><svg width="12" height="10" viewBox="0 0 12 10"><path d="M0 4h12v2a3 3 0 0 1-3 3H3a3 3 0 0 1-3-3z" fill="#6f767b"/><path d="M2 4V1h2" stroke="#6f767b" fill="none"/></svg>2 Bathrooms</span>
      </div>
    </article>
    <article class="listing">
      <div class="thumb" role="img" aria-label="Penthouse terrace with pool and loungers" style="background:linear-gradient(135deg,#9fc7d6,#5f8aa0)"></div>
      <div class="listing-body">
        <h3>Luxury Penthouse</h3>
        <p>We are one of the best agents in the area that genuinely are specialist in both sales and lettings.</p>
        <div class="price">$500,000</div>
      </div>
      <div class="listing-meta">
        <span><svg width="14" height="9" viewBox="0 0 14 9"><path d="M0 0v9M0 6h14v3M3 3h10v3" stroke="#6f767b" fill="none" stroke-width="1.4"/></svg>3 Bedrooms</span>
        <span><svg width="12" height="10" viewBox="0 0 12 10"><path d="M0 4h12v2a3 3 0 0 1-3 3H3a3 3 0 0 1-3-3z" fill="#6f767b"/><path d="M2 4V1h2" stroke="#6f767b" fill="none"/></svg>2 Bathrooms</span>
      </div>
    </article>
    <article class="listing">
      <div class="thumb" role="img" aria-label="Resort apartment block with pool and palms" style="background:linear-gradient(135deg,#8ecbe0,#c7a985)"></div>
      <div class="listing-body">
        <h3>City appartment</h3>
        <p>We are one of the best agents in the area that genuinely are specialist in both sales and lettings.</p>
        <div class="price">$500,000</div>
      </div>
      <div class="listing-meta">
        <span><svg width="14" height="9" viewBox="0 0 14 9"><path d="M0 0v9M0 6h14v3M3 3h10v3" stroke="#6f767b" fill="none" stroke-width="1.4"/></svg>3 Bedrooms</span>
        <span><svg width="12" height="10" viewBox="0 0 12 10"><path d="M0 4h12v2a3 3 0 0 1-3 3H3a3 3 0 0 1-3-3z" fill="#6f767b"/><path d="M2 4V1h2" stroke="#6f767b" fill="none"/></svg>2 Bathrooms</span>
      </div>
    </article>
    <article class="listing">
      <div class="thumb" role="img" aria-label="Terracotta villa with pool at dusk" style="background:linear-gradient(135deg,#d7a277,#6c8ea6)"></div>
      <div class="listing-body">
        <h3>New York City Loft</h3>
        <p>We are one of the best agents in the area that genuinely are specialist in both sales and lettings.</p>
        <div class="price">$500,000</div>
      </div>
      <div class="listing-meta">
        <span><svg width="14" height="9" viewBox="0 0 14 9"><path d="M0 0v9M0 6h14v3M3 3h10v3" stroke="#6f767b" fill="none" stroke-width="1.4"/></svg>3 Bedrooms</span>
        <span><svg width="12" height="10" viewBox="0 0 12 10"><path d="M0 4h12v2a3 3 0 0 1-3 3H3a3 3 0 0 1-3-3z" fill="#6f767b"/><path d="M2 4V1h2" stroke="#6f767b" fill="none"/></svg>2 Bathrooms</span>
      </div>
    </article>
  </div>
  <span class="load-more">Load More</span>
</section>

<section class="featured">
  <div class="wrap">
    <div class="section-head">
      <h2>FEATURED PROPERTY</h2>
      <p>Hand-picked homes our leasing team recommends this month.</p>
    </div>
    <div class="featured-grid">
      <article class="feature-card">
        <div class="thumb" role="img" aria-label="Resort apartment block with pool and palms" style="background:linear-gradient(135deg,#8ecbe0,#c7a985)"></div>
        <div class="feature-body"><h3>City appartment</h3><p>It is a long established fact that a reader will be distracted</p><div class="price">$500,000</div></div>
      </article>
      <article class="feature-card">
        <div class="thumb" role="img" aria-label="Bright loft living room with yellow sofa" style="background:linear-gradient(135deg,#e7c66a,#b78a52)"></div>
        <div class="feature-body"><h3>New York City Loft</h3><p>It is a long established fact that a reader will be distracted</p><div class="price">$500,000</div></div>
      </article>
      <article class="feature-card">
        <div class="thumb" role="img" aria-label="Penthouse terrace with pool and loungers" style="background:linear-gradient(135deg,#9fc7d6,#5f8aa0)"></div>
        <div class="feature-body"><h3>Luxury Penthouse</h3><p>It is a long established fact that a reader will be distracted</p><div class="price">$500,000</div></div>
      </article>
      <article class="feature-card">
        <div class="thumb" role="img" aria-label="Terracotta villa with pool at dusk" style="background:linear-gradient(135deg,#d7a277,#6c8ea6)"></div>
        <div class="feature-body"><h3>City appartment</h3><p>It is a long established fact that a reader will be distracted</p><div class="price">$500,000</div></div>
      </article>
    </div>
  </div>
</section>

<section class="lower">
  <div class="wrap">
    <div class="news">
      <h2 class="col-head">LATEST NEWS</h2>
      <article class="news-item">
        <div class="thumb" role="img" aria-label="Beach huts under a bright sky" style="background:linear-gradient(180deg,#8ccbe6,#d9b98a)"></div>
        <div>
          <h3>Resources that we thought you may find useful</h3>
          <div class="date">28 July, 2015</div>
          <p>It is a long established fact that a reader will be distracted by the readable content of a page when looking at its layout.</p>
        </div>
      </article>
      <article class="news-item">
        <div class="thumb" role="img" aria-label="Tropical resort with palm trees" style="background:linear-gradient(180deg,#7fc2dc,#6f9a5c)"></div>
        <div>
          <h3>What about your next vaction?</h3>
          <div class="date">28 July, 2015</div>
          <p>It is a long established fact that a reader will be distracted by the readable content of a page when looking at its layout.</p>
        </div>
      </article>
    </div>
    <div class="testimonial">
      <h2 class="col-head">WHAT DID YOUR CLIENTS SAY</h2>
      <blockquote class="quote-box">"We feel more than happy with how smoothly the lease went, thank you. The team was quick to answer every question, kept us informed at each step and found us a lovely home near campus. We can easily recommend them to anyone looking for a stress-free move."</blockquote>
      <div class="client">
        <span class="client-name">Corwin Adlesby</span>
        <div class="avatar" role="img" aria-label="Client portrait"></div>
      </div>
    </div>
  </div>
</section>

<footer class="site-footer">
  <div class="wrap">
    <div class="foot-col foot-about">
      <div class="brand"><span class="brand-mark"></span>QWRB Holdings</div>
      <p>It is a long established fact that a reader will be distracted by the readable content of a page when looking at its layout. The point of using placeholder text is that it has a more-or-less normal distribution of letters.</p>
      <span class="more">Read More About Us »</span>
    </div>
    <div class="foot-col foot-links">
      <h4>Quick links</h4>
      <ul><li>Home</li><li>About Us</li><li>Properties</li><li>News</li><li>Services</li><li>Contact Us</li></ul>
    </div>
    <div class="foot-col foot-news">
      <h4>Newsletter</h4>
      <p>Sign up to receive our latest listings and leasing news.</p>
      <div class="foot-input">Enter your Email</div>
      <span class="foot-submit">SUBMIT</span>
    </div>
    <div class="foot-col foot-contact">
      <h4>Contact Info</h4>
      <div class="contact-row"><span class="ico"><svg viewBox="0 0 12 12"><path d="M2.5 1l2 2.5-1.2 1.2a7 7 0 0 0 4 4l1.2-1.2 2.5 2-1.3 1.5C5 11 1 7 1 2.3z" fill="#a9b8bf"/></svg></span>+1 (203) 555 0148</div>
      <div class="contact-row"><span class="ico"><svg viewBox="0 0 12 12"><rect x="1" y="2.5" width="10" height="7" fill="none" stroke="#a9b8bf"/><path d="M1 2.5l5 4 5-4" fill="none" stroke="#a9b8bf"/></svg></span>info@qwrbholdings.com</div>
      <div class="contact-row"><span class="ico"><svg viewBox="0 0 12 12"><path d="M6 11S2 6.8 2 4.5a4 4 0 0 1 8 0C10 6.8 6 11 6 11z" fill="#a9b8bf"/><circle cx="6" cy="4.5" r="1.4" fill="#253a44"/></svg></span>18 Harrowdene Street, New Haven, CT</div>
    </div>
  </div>
</footer>
<div class="copyright">Copyright © 2015 - QWRB Holdings. All Rights Reserved</div>

</body>
</html>
```